Stationery design for software development / consultancy company

We need stationary design based on company logo.

We are based in London, UK and we are providing integration solutions development / consultancy services for VEQ integration projects across UK.

Our name refers two words - integration and grace - and it shows our clients our main specialization field and key characteristics of our solutions / products. We also would like to be associated with follow words: smart, reliable, unique.

Project delivery should include:
- Powerpoint template (needs to have a Cover Page, Table of Contents, 1-2 sample pages, and a Closing/Summary slide at the end)
- Letterhead A4 (Word template)
- Standard invoice A4 (Word template)
- With Compliments Slips A5 (Word template)
- Business card (adobe illustrator)

Attached is logo in vector (please use logo with white background!) and company details for printed stationery.

highly skilled IT professionals

Software

• Clear background in all A4/A5 documents.
All text should be editable, i.e. I will need sources.
• I would prefer light, web 2.0 style colours, follow are in my main interest:
- combination of light grey and orange
- Logo colours
• Please no watermarks on printed stationary

```html
<!DOCTYPE html>
<html lang="en">
<head>
<meta charset="utf-8">
<title>Linkward – Invoice</title>
<link rel="stylesheet" href="https://fonts.googleapis.com/css2?family=Tinos:ital,wght@0,400;0,700;1,400&family=Arimo:ital@1&display=swap">
<style>
  :root {
    --backdrop: #2b2b2b;
    --paper: #ffffff;
    --ink: #111111;
    --rule: #1a1a1a;
    --brand-orange: #e9873a;
    --brand-grey: #5a5f66;
  }
  * { box-sizing: border-box; margin: 0; padding: 0; }
  html, body { width: 1200px; height: 844px; overflow: hidden; background: var(--backdrop); }
  body { position: relative; font-family: "Tinos", "Times New Roman", serif; color: var(--ink); }

  .sheet { position: absolute; left: 296px; top: 52px; width: 593px; height: 767px; background: var(--paper); }
  .abs { position: absolute; }

  .brand { left: 0; width: 100%; top: 20px; display: flex; justify-content: center; align-items: center; gap: 9px; }
  .brand-dot { width: 28px; height: 28px; border-radius: 50%; background: var(--brand-orange); }
  .brand-name { font-size: 33px; font-weight: 400; color: var(--brand-grey); letter-spacing: 0.3px; line-height: 1; }

  .company-address { left: 0; width: 100%; top: 62px; text-align: center; font-size: 9.5px; line-height: 13.5px; }

  .box { border: 1.3px solid var(--rule); font-size: 10.5px; }
  .customer { left: 28px; top: 134px; width: 225px; height: 99px; }
  .customer-head { font-weight: 700; padding: 1px 5px; border-bottom: 1.3px solid var(--rule); height: 16px; line-height: 14px; }
  .customer-row { padding: 0 5px; height: 19px; line-height: 20px; }

  .meta { left: 342px; top: 134px; width: 221px; height: 99px; display: grid; grid-template-columns: 91px 1fr; grid-template-rows: repeat(3, 1fr); }
  .meta-label { border-right: 1.3px solid var(--rule); display: flex; align-items: center; justify-content: center; }
  .meta-label, .meta-value { border-bottom: 1.3px solid var(--rule); }
  .meta > :nth-last-child(-n+2) { border-bottom: none; }

  .doc-title { left: 0; width: 593px; top: 236px; text-align: center; font-size: 22px; font-weight: 700; letter-spacing: 0.5px; }

  .items { left: 28px; top: 272px; width: 535px; height: 235px; border-collapse: collapse; font-size: 11px; table-layout: fixed; }
  .items th { height: 19px; font-weight: 700; border: 1.3px solid var(--rule); padding: 0; line-height: 16px; }
  .items td { border-left: 1.3px solid var(--rule); border-right: 1.3px solid var(--rule); border-bottom: 1.3px solid var(--rule); }

  .totals { left: 413px; top: 509px; width: 150px; height: 79px; border-collapse: collapse; font-size: 10px; table-layout: fixed; }
  .totals td { border: 1.3px solid var(--rule); height: 26px; padding: 0 3px; }
  .totals .label { text-align: right; width: 71px; }

  .terms { left: 36px; top: 553px; width: 372px; font-family: "Arimo", Arial, sans-serif; font-style: italic; font-size: 7.6px; line-height: 11px; }

  .signoff { left: 36px; font-size: 11px; font-weight: 700; }
  .signoff-thanks { top: 627px; }
  .signoff-name { top: 653px; }
  .signoff-role { top: 680px; }
</style>
</head>
<body>
  <main class="sheet">
    <header class="brand abs">
      <span class="brand-dot"></span>
      <span class="brand-name">linkward</span>
    </header>
    <address class="company-address abs" style="font-style: normal;">
      Linkward Limited, 42 Elm Court<br>
      118 Marlow Lane, London<br>
      SE9 4RT, United Kingdom<br>
      Tel.: +44(0)20 7946 0815
    </address>

    <section class="customer box abs">
      <div class="customer-head">Customer</div>
      <div class="customer-row">Name :</div>
      <div class="customer-row">Address1 :</div>
      <div class="customer-row">Address2:</div>
      <div class="customer-row">Mobile :</div>
    </section>

    <section class="meta box abs">
      <div class="meta-label">Invoice No.</div><div class="meta-value"></div>
      <div class="meta-label">Date</div><div class="meta-value"></div>
      <div class="meta-label">Order No.</div><div class="meta-value"></div>
    </section>

    <h1 class="doc-title abs">INVOICE</h1>

    <table class="items abs">
      <colgroup>
        <col style="width:49px"><col style="width:257px"><col style="width:79px"><col style="width:71px"><col style="width:79px">
      </colgroup>
      <thead>
        <tr><th>Sl No.</th><th>Description</th><th>Price</th><th>Quantity</th><th>Total</th></tr>
      </thead>
      <tbody>
        <tr><td></td><td></td><td></td><td></td><td></td></tr>
      </tbody>
    </table>

    <table class="totals abs">
      <tr><td class="label">Subtotal</td><td></td></tr>
      <tr><td class="label">Tax</td><td></td></tr>
      <tr><td class="label">Total</td><td></td></tr>
    </table>

    <p class="terms abs">All prices are final and not negotiable. Payments must be made by the agreed due date without exceptions. Posted cheques will be treated as late if the postmark date is after the due date above.</p>

    <p class="signoff signoff-thanks abs">Thanks</p>
    <p class="signoff signoff-name abs">Daniel Hartley</p>
    <p class="signoff signoff-role abs">Director</p>
  </main>
</body>
</html>
```